Modern Business Card for Industrial Company

We need business cards updated with modern fonts and make it look more technical, sharp and clean. The logo should not be changed, but we are looking for fresh solutions for how other information on the card is laid out in an interesting way. The company provides machinery and services to the ceramic industry and deals with cutting-edge technology. The design should reflect a technologically advanced and modern company that deals with the latest European technologies.

Font styles to use
Sans Serif

Requirements
Must have
• Modern fonts, technical look and feel

```html
<!DOCTYPE html>
<html lang="en">
<head>
<meta charset="utf-8">
<title>Torvale Service — Business Card</title>
<link href="https://fonts.googleapis.com/css2?family=Open+Sans:wght@400;700&display=swap" rel="stylesheet">
<style>
  :root {
    --backdrop: #3a3a3a;
    --card: #161616;
    --card-pattern: #1d1d1d;
    --edge: #0c5fb0;
    --brand-blue: #1466b4;
    --text-grey: #c9c9c9;
    --icon-red: #c8262c;
  }
  * { box-sizing: border-box; margin: 0; padding: 0; }
  html, body { width: 1200px; height: 801px; overflow: hidden; }
  body {
    background: var(--backdrop);
    font-family: "Open Sans", Arial, sans-serif;
    position: relative;
  }
  .card {
    position: absolute;
    width: 520px;
    height: 297px;
    background: var(--card);
    border-bottom: 3px solid var(--edge);
    border-right: 2px solid var(--edge);
    box-shadow: 0 10px 24px rgba(0,0,0,.45);
    overflow: hidden;
  }
  .card-front { left: 50px; top: 252px; }
  .card-back { left: 630px; top: 252px; }

  .brand {
    position: absolute;
    left: 34px;
    top: 92px;
    display: flex;
    align-items: center;
    gap: 10px;
  }
  .brand-mark { width: 14px; height: 14px; background: var(--icon-red); }
  .brand-name {
    font-weight: 700;
    font-size: 30px;
    letter-spacing: 1px;
    color: var(--brand-blue);
  }

  .person {
    position: absolute;
    right: 30px;
    top: 60px;
    text-align: right;
  }
  .person-name {
    font-weight: 700;
    font-size: 18px;
    letter-spacing: .5px;
    color: var(--brand-blue);
    text-transform: uppercase;
  }
  .person-title { font-size: 13px; color: var(--text-grey); margin-top: -2px; }

  .divider {
    position: absolute;
    left: 34px;
    right: 30px;
    top: 176px;
    height: 1px;
    background: var(--brand-blue);
  }

  .address {
    position: absolute;
    right: 30px;
    top: 110px;
    text-align: right;
    font-size: 13px;
    line-height: 18px;
    color: var(--text-grey);
  }

  .contacts {
    position: absolute;
    left: 34px;
    top: 192px;
    list-style: none;
    font-size: 13px;
    line-height: 20px;
    color: var(--text-grey);
  }
  .contacts li { display: flex; align-items: center; gap: 8px; }
  .contacts svg { width: 11px; height: 11px; fill: var(--icon-red); flex: none; }

  .back-pattern {
    position: absolute;
    inset: 0;
    background: linear-gradient(135deg, #121212 0%, var(--card-pattern) 55%, #262626 100%);
  }
  .back-brand {
    position: absolute;
    right: 70px;
    bottom: 86px;
    font-weight: 700;
    font-size: 24px;
    letter-spacing: 1px;
    color: var(--brand-blue);
  }
</style>
</head>
<body>
  <section class="card card-front">
    <div class="brand">
      <span class="brand-mark"></span>
      <span class="brand-name">TORVALE</span>
    </div>

    <div class="person">
      <p class="person-name">Marco Ferrante</p>
      <p class="person-title">President</p>
    </div>

    <address class="address" style="font-style:normal; top:120px;">
      418 Kiln Avenue, Suite 200<br>
      Ridgefield, GA 30112
    </address>

    <div class="divider"></div>

    <ul class="contacts">
      <li>
        <svg viewBox="0 0 24 24" aria-hidden="true"><path d="M6.6 10.8a15.1 15.1 0 0 0 6.6 6.6l2.2-2.2a1 1 0 0 1 1-.25 11.4 11.4 0 0 0 3.6.57 1 1 0 0 1 1 1V20a1 1 0 0 1-1 1A17 17 0 0 1 3 4a1 1 0 0 1 1-1h3.5a1 1 0 0 1 1 1c0 1.25.2 2.45.57 3.57a1 1 0 0 1-.25 1z"/></svg>
        (555) 214.6037
      </li>
      <li>
        <svg viewBox="0 0 24 24" aria-hidden="true"><path d="M2 5h20v14H2zm2 2v.5l8 5 8-5V7l-8 5z"/></svg>
        mferrante@torvale.com
      </li>
      <li>
        <svg viewBox="0 0 24 24" aria-hidden="true"><circle cx="12" cy="12" r="10"/></svg>
        www.torvale.com
      </li>
    </ul>
  </section>

  <section class="card card-back">
    <div class="back-pattern" role="img" aria-label="Tone-on-tone repeating monogram pattern across the card back"></div>
    <span class="back-brand">TORVALE</span>
  </section>
</body>
</html>
```